New eyelid plastic surgery office needs a business card design-Eyelid Surgery Partners of Brennor

I recently used SketchHarbor for my logo design and was very pleased with creativity and results. It was a difficult decision for me. Now I would like to create a business card based on this logo, which I will attach.

The text should be easily legible as some of my patients have difficulty seeing, but I would like a subtle, sophisticated artistry also evident to make the card memorable. Would like the card based on a similar color scheme as the logo but the inverse or other complementary colors may prove interesting

A good question was asked...my concern about my visually impaired patients was really my desire to avoid italicized or calligraphic type fonts that may be hard to read. Standard font size for a business card would be fine. Thanks!

Thank you so much for the great work so far. I wanted to give you my particular contact information to see if that would change the look of the cards. Martin Pellowby, MD Address: 2817 Larkmoor Avenue, Suite 205 Wilmington, NC 28517 Phone: 910-555-0183 Fax: 910-555-0184 Website: www.brennorlidclinic.example Please delete the email slot from the card. Thanks so much!

Reason: Last minute consideration. So many great revisions right now!

Plastic

```html
<!DOCTYPE html>
<html lang="en">
<head>
<meta charset="utf-8">
<title>Eyelid Surgery Partners of Brennor – Business Card</title>
<link rel="stylesheet" href="https://fonts.googleapis.com/css2?family=Open+Sans:wght@400;600;700&display=swap">
<style>
  :root {
    --page-bg: #e8e8ea;
    --card-white: #ffffff;
    --brand-blue: #0b4f9f;
    --swoosh-grey: #c9cacc;
    --contact-text: #ffffff;
  }
  * { margin: 0; padding: 0; box-sizing: border-box; }
  html, body {
    width: 1200px;
    height: 900px;
    overflow: hidden;
    background: var(--page-bg);
    font-family: "Open Sans", Arial, sans-serif;
  }
  .canvas {
    position: relative;
    width: 1200px;
    height: 900px;
  }
  .business-card {
    position: absolute;
    left: 120px;
    top: 176px;
    width: 960px;
    height: 548px;
    background: var(--card-white);
    overflow: hidden;
    box-shadow: 0 6px 18px rgba(0, 0, 0, 0.18);
  }
  .card-shapes {
    position: absolute;
    inset: 0;
    width: 100%;
    height: 100%;
  }
  .card-shapes .swoosh { fill: var(--swoosh-grey); }
  .card-shapes .blue-field { fill: var(--brand-blue); }
  .practice-name {
    position: absolute;
    left: 48px;
    top: 72px;
    color: var(--brand-blue);
    font-weight: 400;
    font-size: 28px;
    line-height: 40px;
    letter-spacing: 1px;
    text-transform: uppercase;
  }
  .contact-details {
    position: absolute;
    right: 66px;
    top: 262px;
    text-align: right;
    color: var(--contact-text);
    font-style: normal;
  }
  .contact-details .phone {
    font-weight: 700;
    font-size: 38px;
    line-height: 52px;
    margin-bottom: 2px;
  }
  .contact-details .line {
    font-weight: 400;
    font-size: 31px;
    line-height: 46px;
  }
  .contact-details .line.tight { line-height: 44px; }
</style>
</head>
<body>
<main class="canvas">
  <section class="business-card" aria-label="Business card front">
    <svg class="card-shapes" viewBox="0 0 350 200" preserveAspectRatio="none" aria-hidden="true">
      <path class="swoosh" d="M0 150 C 75 128, 150 74, 206 4 L 210 0 C 150 70, 72 142, 0 172 Z"/>
      <path class="blue-field" d="M210 0 L350 0 L350 200 L0 200 L0 172 C 72 142, 150 70, 210 0 Z"/>
    </svg>

    <h1 class="practice-name">
      Eyelid Surgery<br>Partners of Brennor
    </h1>

    <address class="contact-details">
      <p class="phone">000 000 000</p>
      <p class="line">Build, Street,</p>
      <p class="line">0000 00 City</p>
      <p class="line tight">email@site.example</p>
      <p class="line tight">www.site.example</p>
    </address>
  </section>
</main>
</body>
</html>
```